Flyer 2 Seiten Pflegestufe
Zielgruppe
Es handelt sich um einen mobilen Pflegedienst. Wir versorgen die Patienten ambulant in der Häuslichkeit. Im Mittelpunkt steht immer der Patient.

```html
<!DOCTYPE html>
<html lang="de">
<head>
<meta charset="utf-8">
<title>Pflegehaus Ostwind – Flyer</title>
<link href="https://fonts.googleapis.com/css2?family=Arimo:wght@400;700&display=swap" rel="stylesheet">
<style>
  :root {
    --orange: #f2952f;
    --green: #6aae38;
    --blue: #0b5aa0;
    --ink: #111111;
    --paper: #ffffff;
    --bg-light: #f6f7f9;
    --bg-mid: #dfe3e8;
  }
  html, body { margin: 0; padding: 0; overflow: hidden; }
  body { width: 1200px; height: 851px; font-family: "Arimo", Arial, sans-serif; color: var(--ink); }
  .flyer {
    position: relative; width: 1200px; height: 851px; overflow: hidden;
    background:
      radial-gradient(circle at 95% 20%, rgba(255,255,255,.9) 0 6%, transparent 22%),
      radial-gradient(circle at 20% 75%, rgba(255,255,255,.95) 0 10%, transparent 30%),
      radial-gradient(ellipse at 70% 90%, rgba(255,255,255,.8) 0 10%, transparent 40%),
      linear-gradient(160deg, var(--bg-light) 0%, var(--bg-mid) 45%, var(--bg-light) 70%, var(--bg-mid) 100%);
  }
  .bokeh { position: absolute; border-radius: 50%; background: rgba(255,255,255,.75); box-shadow: 0 0 12px rgba(255,255,255,.9); }
  .section-title {
    position: absolute; top: 60px; height: 48px; margin: 0;
    background: var(--orange); color: var(--paper); border-radius: 6px;
    font-weight: 400; font-size: 25px; line-height: 48px; padding-left: 13px; box-sizing: border-box;
  }
  .title-left { left: 54px; width: 489px; }
  .title-right { left: 600px; width: 551px; padding-left: 11px; }
  .panel {
    position: absolute; top: 132px; background: var(--paper); border-radius: 6px;
    font-size: 21px; line-height: 27.5px; box-sizing: border-box;
  }
  .panel p { margin: 0 0 27.5px; }
  .panel-intro { left: 54px; width: 489px; height: 415px; padding: 24px 0 0 10px; }
  .panel-services { left: 600px; width: 551px; height: 649px; padding: 24px 0 0 10px; }
  .ticks { position: absolute; left: 566px; top: 170px; }
  .rule { position: absolute; }
  .rule-green { left: 305px; top: 783px; width: 895px; height: 4px; background: var(--green); }
  .rule-blue { left: 0; top: 825px; width: 958px; height: 4px; background: var(--blue); }
  .brand { position: absolute; left: 50px; top: 578px; width: 240px; text-align: center; }
  .brand-circle { width: 144px; height: 144px; margin: 0 auto; border: 8px solid var(--blue); border-radius: 50%; box-sizing: border-box; background: var(--paper); }
  .brand-name { margin-top: 14px; font-size: 26px; font-weight: 700; color: var(--blue); line-height: 30px; }
</style>
</head>
<body>
<main class="flyer">
  <span class="bokeh" style="left:1175px;top:180px;width:10px;height:10px"></span>
  <span class="bokeh" style="left:1120px;top:260px;width:30px;height:30px;opacity:.6"></span>
  <span class="bokeh" style="left:275px;top:545px;width:36px;height:36px;opacity:.7"></span>
  <span class="bokeh" style="left:785px;top:795px;width:30px;height:30px;opacity:.6"></span>
  <span class="bokeh" style="left:885px;top:798px;width:28px;height:28px;opacity:.6"></span>
  <span class="bokeh" style="left:965px;top:798px;width:30px;height:30px;opacity:.7"></span>
  <span class="bokeh" style="left:20px;top:700px;width:34px;height:34px;opacity:.5"></span>

  <h2 class="section-title title-left">Ihr Pflegehaus Ostwind in Rostock</h2>
  <h2 class="section-title title-right">Wir unterstützen Sie gerne</h2>

  <section class="panel panel-intro">
    <p><strong>Wenn ein hilfsbedürftiger Mensch und<br>dessen Angehörige in einer Pflegesituation<br>Hilfe benötigen, stellen sich viele Fragen:</strong></p>
    <p>Wer unterstützt mich im Alltag? Wie kann<br>ich mein bisheriges Leben in vertrauter<br>Atmosphäre weiterleben? Wo bekomme ich<br>Hilfsmittel? Welche Anträge muss ich stellen?</p>
    <p>Auf diese und andere Fragen bekommen Sie<br>in Ihrem Pflegehaus-Ostwind eine Antwort.<br>Wir kümmern uns darum, dass Sie so lange<br>wie möglich in ihren eigenen vier Wänden<br>bleiben können.</p>
  </section>

  <svg class="ticks" width="34" height="360" viewBox="0 0 34 360" aria-hidden="true">
    <g fill="none" stroke="rgba(255,255,255,.85)" stroke-width="6" stroke-linecap="round" stroke-linejoin="round">
      <path d="M4 16 L13 28 L30 2"/>
      <path d="M4 98 L13 110 L30 84"/>
      <path d="M4 181 L13 193 L30 167"/>
      <path d="M4 263 L13 275 L30 249"/>
      <path d="M4 345 L13 357 L30 331"/>
    </g>
  </svg>

  <section class="panel panel-services">
    <p>Wir helfen Ihnen dabei, <strong>möglichst lange<br>im eigenen Zuhause verbleiben</strong> zu können</p>
    <p>Wir unterstützen <strong>kostenlos</strong> bei der<br><strong>Beantragung einer Pflegestufe</strong></p>
    <p>Wir sorgen für die <strong>Vernetzung aller</strong> pflegerischen,<br>medizinischen und sozialen <strong>Leistungen</strong></p>
    <p>Wir schaffen <strong>Transparenz für Betroffene<br>und Angehörige</strong></p>
    <p>Wir <strong>unterstützen</strong> Menschen in <strong>belastenden Situa-<br>tionen</strong>, auch durch <strong>psychosoziale Beratung</strong></p>
    <p>Im Pflegehaus Ostwind erhalten Sie <strong>individuelle<br>und kostenfreie Beratung</strong>. Bei Bedarf<br>erfolgt die Beratung auch bei Ihnen zu Hause.</p>
    <p><strong>Rufen Sie uns kostenfrei an und vereinbaren<br>Sie einen Termin: 0800 47311 26</strong></p>
  </section>

  <div class="rule rule-green"></div>
  <div class="rule rule-blue"></div>

  <div class="brand">
    <div class="brand-circle"></div>
    <div class="brand-name">Pflegehaus Ostwind</div>
  </div>
</main>
</body>
</html>
```